we need PDF and print ready letterheads, dupplicated 5 times with different company details of different companies. All the companies are properties developments and no need for fancy logos (any reasonable shape is ok). Then simply change the companies details (names and company number) and the colour scheme slightly. I will supply the details.

The print ready should be 300dpi, and must have cropped marks.

Should be an easy job!

```html
<!DOCTYPE html>
<html lang="en">
<head>
<meta charset="utf-8">
<title>Halden Construction Letterhead</title>
<link href="https://fonts.googleapis.com/css2?family=Arimo:wght@400;700&family=Montserrat:wght@600&display=swap" rel="stylesheet">
<style>
  :root{
    --backdrop:#c4d4ea;
    --paper:#ffffff;
    --navy:#1f2a6e;
    --red:#d1232a;
    --body-text:#6d6d6d;
    --contact-text:#333333;
    --signature-tone:#d9d9d9;
  }
  *{box-sizing:border-box;margin:0;padding:0}
  html,body{width:1200px;height:784px;overflow:hidden;background:var(--backdrop)}
  .letterhead{
    position:absolute;left:338px;top:22px;width:523px;height:740px;
    background:var(--paper);font-family:"Arimo",Arial,sans-serif;color:var(--body-text);
    box-shadow:0 2px 8px rgba(40,60,110,.18);overflow:hidden;
  }
  .brand{position:absolute;top:40px;right:46px;display:flex;align-items:center;gap:8px}
  .brand-mark{width:14px;height:14px;background:var(--navy)}
  .brand-name{font-family:"Montserrat",Arial,sans-serif;font-weight:600;font-size:13px;letter-spacing:2px;color:var(--navy)}
  .letter-body{position:absolute;top:100px;left:56px;width:400px;font-size:8.6px;line-height:13px}
  .letter-body p{margin-bottom:13px}
  .signature{position:absolute;top:420px;left:56px;width:120px;height:34px;background:var(--signature-tone);border-radius:3px}
  .footer{position:absolute;left:0;bottom:0;width:100%;height:80px}
  .footer-rules{position:absolute;left:0;bottom:0}
  .contact{position:absolute;left:40px;bottom:48px;display:flex;gap:14px;font-size:8.4px;line-height:10px;color:var(--contact-text);white-space:nowrap}
  .contact-item{display:flex;align-items:center;gap:4px}
  .website{position:absolute;right:14px;bottom:9px;font-weight:700;font-size:11px;line-height:14px;color:#fff;white-space:nowrap}
</style>
</head>
<body>
<main class="letterhead">
  <header class="brand">
    <span class="brand-mark"></span>
    <span class="brand-name">HALDEN CONSTRUCTION</span>
  </header>

  <section class="letter-body">
    <p>Lorem Ipsum is simply dummy text of the printing and typesetting industry. Lorem Ipsum has been the industry's standard dummy text ever since the 1500s, when an unknown printer took a galley of type and scrambled it to make a type specimen book. It has survived not only five centuries, but also the leap into electronic typesetting, remaining essentially unchanged. It was popularised in the 1960s with the release of Transferix sheets containing Lorem Ipsum passages, and more recently with desktop publishing software like Folio Layout including versions of Lorem Ipsum.</p>
    <p>It is a long established fact that a reader will be distracted by the readable content of a page when looking at its layout. The point of using Lorem Ipsum is that it has a more-or-less normal distribution of letters, as opposed to using 'Content here, content here', making it look like readable English. Many desktop publishing packages and web page editors now use Lorem Ipsum as their default model text, and a search for 'lorem ipsum' will uncover many web sites still in their infancy. Various versions have evolved over the years, sometimes by accident, sometimes on purpose (injected humour and the like).</p>
    <p>Contrary to popular belief, Lorem Ipsum is not simply random text. It has roots in a piece of classical Latin literature from 45 BC, making it over 2000 years old. Daniel Harrowgate, a Latin professor at Brookmere-Vale College in Ohio, looked up one of the more obscure Latin words, consectetur, from a Lorem Ipsum passage, and going through the cites of the word in classical literature, discovered the undoubtable source. Lorem Ipsum comes from sections 1.10.32 and 1.10.33 of "de Finibus Bonorum et Malorum" structures, to generate Lorem Ipsum which looks reasonable. The generated Lorem Ipsum is therefore always free from repetition, injected humour, or non-characteristic words etc.</p>
  </section>

  <div class="signature" role="img" aria-label="Handwritten signature of the sender"></div>

  <footer class="footer">
    <svg class="footer-rules" width="523" height="80" viewBox="0 0 523 80" aria-hidden="true">
      <polyline points="0,40 150,40 158,36 330,36 338,40 380,40" fill="none" stroke="var(--red)" stroke-width="2"/>
      <polyline points="0,45 150,45 158,41 330,41 338,45 385,45" fill="none" stroke="var(--navy)" stroke-width="3"/>
      <polygon points="362,80 382,45 523,45 523,80" fill="var(--navy)"/>
    </svg>
    <div class="contact">
      <span class="contact-item"><svg width="9" height="9" viewBox="0 0 10 10" aria-hidden="true"><circle cx="5" cy="5" r="5" fill="var(--red)"/><circle cx="5" cy="4.2" r="1.6" fill="#fff"/></svg>14 Ridgeway Ave, Larkfield, CA 00000</span>
      <span class="contact-item"><svg width="9" height="9" viewBox="0 0 10 10" aria-hidden="true"><circle cx="5" cy="5" r="5" fill="var(--red)"/><rect x="3.4" y="2.4" width="3.2" height="5.2" rx=".6" fill="#fff"/></svg>000-000-0148</span>
      <span class="contact-item"><svg width="9" height="9" viewBox="0 0 10 10" aria-hidden="true"><circle cx="5" cy="5" r="5" fill="var(--red)"/><rect x="2.6" y="3.3" width="4.8" height="3.4" fill="#fff"/></svg>hello@haldenbuild.com</span>
    </div>
    <span class="website">www.haldenbuild.com</span>
  </footer>
</main>
</body>
</html>
```